Bref créative
Safety products company
Safety products for life
Professional
Gordon R Pike
President/Founder
482 Wexley Lane
Marlow Hollow, PA 16224-3871
866.41C.TOWN (412.8696)
pike@corvantahome.com
www.corvantahome.com
BE PREPARED
HOME
DISASTER
CHILD
SENIOR
PET
TRAVEL
STAY SECURE
the logo
"stacked" logo - two more will be coming with white backgrounds as soon as I receive them
4 AI LOGOS

```html
<!DOCTYPE html>
<html lang="en">
<head>
<meta charset="utf-8">
<title>Corvanta Home — Business Cards</title>
<link href="https://fonts.googleapis.com/css2?family=Open+Sans:ital,wght@0,400;0,600;0,700;1,400&display=swap" rel="stylesheet">
<style>
  :root{
    --stage:#3a3a3a;
    --card-dark:#333335;
    --card-light:#ffffff;
    --red:#c0261c;
    --red-deep:#7e130d;
    --grey-soft:#b8b8b8;
    --ink-light:#e6e6e6;
    --ink-dark:#4a4a4a;
    --label:#f2f2f2;
  }
  *{margin:0;padding:0;box-sizing:border-box}
  html,body{width:1200px;height:838px;overflow:hidden;background:var(--stage)}
  body{font-family:"Open Sans",Arial,sans-serif;position:relative}

  .card{position:absolute;overflow:hidden}
  .card--dark{background:var(--card-dark);border-radius:6px}
  .card--light{background:var(--card-light);border-radius:16px}
  .front{top:41px;width:542px;height:300px}
  .back{top:413px;width:542px;height:350px}
  .col-left{left:34px}
  .col-right{left:614px}

  .accent-band{position:absolute;top:0;right:0;width:84px;height:100%;
    background:linear-gradient(90deg,var(--grey-soft) 0%,var(--red) 45%,var(--red-deep) 100%)}

  .logo{position:absolute;left:24px;top:38px;display:flex;align-items:center;gap:10px}
  .logo__dot{width:26px;height:26px;border-radius:50%;background:var(--red)}
  .logo__name{font-size:30px;font-weight:600;letter-spacing:1.5px;text-transform:uppercase;line-height:1}
  .card--dark .logo__name{color:var(--ink-light)}
  .card--light .logo__name{color:var(--ink-dark)}

  .identity{position:absolute;left:24px;top:128px}
  .identity__name{font-size:16px;font-style:italic;color:var(--red);line-height:20px}
  .identity__role{font-size:12px;line-height:16px}
  .card--dark .identity__role{color:var(--ink-light)}
  .card--light .identity__role{color:var(--ink-dark)}

  .contacts{position:absolute;left:24px;top:182px;list-style:none;font-size:10px;line-height:14.5px}
  .card--dark .contacts{color:#d2d2d2}
  .card--light .contacts{color:#555}
  .contacts li{display:flex;align-items:center;gap:6px;white-space:nowrap}
  .contacts svg{width:8px;height:8px;flex:none}

  .mark{position:absolute;left:50%;top:118px;width:90px;height:90px;margin-left:-45px;background:var(--red);border-radius:50%;box-shadow:0 6px 10px rgba(0,0,0,.35)}
  .tagline{position:absolute;left:0;right:0;top:256px;text-align:center;font-size:13px;line-height:24px}
  .card--dark .tagline{color:#bdbdbd}
  .card--light .tagline{color:#666}

  .label{position:absolute;width:542px;text-align:center;color:var(--label);font-size:19px;font-variant:small-caps;letter-spacing:3px;font-weight:600;line-height:24px}
  .label--front{top:365px}
  .label--back{top:772px}
</style>
</head>
<body>

<section class="card card--dark front col-left">
  <div class="accent-band" role="img" aria-label="Red and grey curved accent artwork"></div>
  <div class="logo"><span class="logo__dot"></span><span class="logo__name">Corvanta Home</span></div>
  <div class="identity">
    <p class="identity__name">Gordon R Pike</p>
    <p class="identity__role">President | Founder</p>
  </div>
  <ul class="contacts">
    <li><svg viewBox="0 0 10 10"><path d="M2 1 L4 3 L3 4 Q4 6 6 7 L7 6 L9 8 L8 9 Q2 8 1 2 Z" fill="var(--red)"/></svg>866.41C.TOWN (412.8696)</li>
    <li><svg viewBox="0 0 10 10"><path d="M2 1 L4 3 L3 4 Q4 6 6 7 L7 6 L9 8 L8 9 Q2 8 1 2 Z" fill="var(--red)"/></svg>866-412-8696</li>
    <li><svg viewBox="0 0 10 10"><path d="M2 1 L4 3 L3 4 Q4 6 6 7 L7 6 L9 8 L8 9 Q2 8 1 2 Z" fill="var(--red)"/></svg>724-555-0183</li>
    <li><svg viewBox="0 0 10 10"><rect x="2" y="1" width="6" height="8" rx="1" fill="var(--red)"/></svg>724-555-0147</li>
    <li><svg viewBox="0 0 10 10"><rect x="1" y="2" width="8" height="6" fill="var(--red)"/></svg>pike@corvantahome.com</li>
    <li><svg viewBox="0 0 10 10"><circle cx="5" cy="5" r="4" fill="var(--red)"/></svg>www.corvantahome.com</li>
    <li><svg viewBox="0 0 10 10"><path d="M5 1 A3 3 0 0 1 8 4 Q8 6 5 9 Q2 6 2 4 A3 3 0 0 1 5 1 Z" fill="var(--red)"/></svg>482 Wexley Lane Marlow Hollow, PA 16224-3871</li>
  </ul>
</section>

<section class="card card--light front col-right">
  <div class="accent-band" role="img" aria-label="Red and grey curved accent artwork"></div>
  <div class="logo"><span class="logo__dot"></span><span class="logo__name">Corvanta Home</span></div>
  <div class="identity">
    <p class="identity__name">Gordon R Pike</p>
    <p class="identity__role">President | Founder</p>
  </div>
  <ul class="contacts">
    <li><svg viewBox="0 0 10 10"><path d="M2 1 L4 3 L3 4 Q4 6 6 7 L7 6 L9 8 L8 9 Q2 8 1 2 Z" fill="var(--red)"/></svg>866.41C.TOWN (412.8696)</li>
    <li><svg viewBox="0 0 10 10"><path d="M2 1 L4 3 L3 4 Q4 6 6 7 L7 6 L9 8 L8 9 Q2 8 1 2 Z" fill="var(--red)"/></svg>866-412-8696</li>
    <li><svg viewBox="0 0 10 10"><path d="M2 1 L4 3 L3 4 Q4 6 6 7 L7 6 L9 8 L8 9 Q2 8 1 2 Z" fill="var(--red)"/></svg>724-555-0183</li>
    <li><svg viewBox="0 0 10 10"><rect x="2" y="1" width="6" height="8" rx="1" fill="var(--red)"/></svg>724-555-0147</li>
    <li><svg viewBox="0 0 10 10"><rect x="1" y="2" width="8" height="6" fill="var(--red)"/></svg>pike@corvantahome.com</li>
    <li><svg viewBox="0 0 10 10"><circle cx="5" cy="5" r="4" fill="var(--red)"/></svg>www.corvantahome.com</li>
    <li><svg viewBox="0 0 10 10"><path d="M5 1 A3 3 0 0 1 8 4 Q8 6 5 9 Q2 6 2 4 A3 3 0 0 1 5 1 Z" fill="var(--red)"/></svg>482 Wexley Lane Marlow Hollow, PA 16224-3871</li>
  </ul>
</section>

<p class="label label--front" style="left:34px">Business Card Front</p>
<p class="label label--front" style="left:614px">Business Card Front</p>

<section class="card card--dark back col-left">
  <span class="mark"></span>
  <p class="tagline">Be Prepared | Home | Disaster | Child | Senior | Pet<br>Travel | Stay Secure</p>
</section>

<section class="card card--light back col-right">
  <span class="mark"></span>
  <p class="tagline">Be Prepared | Home | Disaster | Child | Senior | Pet<br>Travel | Stay Secure</p>
</section>

<p class="label label--back" style="left:34px">Business Card Back</p>
<p class="label label--back" style="left:614px">Business Card Back</p>

</body>
</html>
```